Finding the Steadfast Female Athlete

I am making an athlete version of the book cover that you created before. I need a few modifications to the book, to differentiate the covers. I am not sure what I am looking for, but I would want some fom of "Athlete Version" of this book to differentiate from the parent addition I created before.

Target Market(s)

Female Athletes between 14-22, Parents of Female Athletes 12-22

Font styles to use
Sans Serif

Requirements
Must have
• The same vibe as the previous book cover. I need some differentiation, but keeping the same theme

```html
<!DOCTYPE html>
<html lang="en">
<head>
<meta charset="utf-8">
<title>Finding the Steadfast Female Athlete – Cover Wrap</title>
<link href="https://fonts.googleapis.com/css2?family=Anton&family=Oswald:wght@400;500&family=Montserrat:wght@500;700&family=Arimo:wght@400;700&display=swap" rel="stylesheet">
<style>
  :root{
    --page:#2b2b2b;
    --cover-dark:#161a1c;
    --cover-mid:#23292c;
    --ink:#f2f2f2;
    --ink-soft:#d9d9d9;
    --gold:#d9a92a;
    --gold-light:#f1d36a;
    --gold-deep:#8a6a12;
    --photo-skin:#5d5a52;
    --photo-top:#3b4347;
  }
  *{margin:0;padding:0;box-sizing:border-box}
  html,body{width:837px;height:1200px;overflow:hidden;background:var(--page)}
  .wrap{
    position:absolute;left:18px;top:313px;width:800px;height:573px;
    background:linear-gradient(160deg,var(--cover-mid),var(--cover-dark) 70%);
    overflow:hidden;
  }
  .panel{position:absolute;top:0;height:100%}
  .back-cover{left:0;width:377px}
  .spine{left:377px;width:46px}
  .front-cover{left:423px;width:377px}

  .kicker{
    font-family:"Oswald",sans-serif;font-weight:500;color:var(--ink);
    text-transform:uppercase;text-align:center;letter-spacing:.32em;
  }
  .title-word{display:block;margin:0 auto}
  .title-word text{font-family:"Anton",sans-serif;fill:url(#gold)}

  /* back */
  .back-cover .kicker.top{position:absolute;top:11px;left:0;width:377px;font-size:15px}
  .back-cover .title-word{position:absolute;top:28px;left:81px}
  .back-cover .kicker.sub{position:absolute;top:112px;left:0;width:377px;font-size:14px}
  .blurb{
    position:absolute;left:22px;top:139px;width:336px;
    font-family:"Arimo",sans-serif;font-size:8.6px;line-height:10.6px;color:var(--ink-soft);
    text-align:justify;
  }
  .blurb p{margin-bottom:10px}
  .blurb strong{color:var(--ink)}
  .about-heading{
    display:flex;align-items:center;gap:8px;margin:-2px 6px 6px 6px;
    font-family:"Arimo",sans-serif;font-weight:700;font-size:10px;color:var(--gold);
  }
  .about-heading::before,.about-heading::after{content:"";flex:1;height:1px;background:var(--gold)}
  .about-heading::before{flex:0 0 110px}
  .author-photo{
    float:left;width:94px;height:94px;margin:0 8px 4px 0;
    background:radial-gradient(circle at 50% 45%,#6b6258,#2a2a2a 70%);
  }
  .imprint{
    position:absolute;left:14px;bottom:22px;display:flex;align-items:center;gap:6px;
    font-family:"Montserrat",sans-serif;font-weight:700;font-size:8px;color:var(--ink);letter-spacing:.05em;
  }
  .imprint .dot{width:20px;height:20px;border-radius:50%;border:1.5px solid var(--gold)}

  /* spine */
  .spine-title{
    position:absolute;top:12px;left:14px;writing-mode:vertical-rl;
    font-family:"Oswald",sans-serif;font-weight:500;font-size:13px;color:var(--ink);letter-spacing:.04em;
  }
  .spine-title .gold{color:var(--gold)}
  .spine-mark{position:absolute;top:297px;left:12px;width:22px;height:22px;border-radius:50%;border:1.5px solid var(--gold)}
  .spine-author{
    position:absolute;top:374px;left:14px;writing-mode:vertical-rl;
    font-family:"Montserrat",sans-serif;font-weight:700;font-size:13px;color:var(--ink);letter-spacing:.5em;
  }

  /* front */
  .cover-photo{
    position:absolute;inset:0;
    background:
      radial-gradient(ellipse 45% 55% at 52% 42%,var(--photo-skin),transparent 70%),
      radial-gradient(ellipse 70% 60% at 50% 30%,var(--photo-top),var(--cover-dark) 80%);
  }
  .front-cover .kicker.top{position:absolute;top:450px;left:0;width:377px;font-size:24px;top:448px}
  .front-cover .title-word{position:absolute;top:270px;left:31px}
  .front-cover .kicker.sub{position:absolute;top:402px;left:0;width:377px;font-size:22px}
  .front-cover .kicker.top{top:236px}
  .tagline{
    position:absolute;top:441px;left:0;width:377px;text-align:center;
    font-family:"Montserrat",sans-serif;font-weight:500;font-size:9.4px;line-height:11.6px;
    letter-spacing:.22em;color:var(--ink);text-transform:uppercase;
  }
  .tagline .ring{border:1px solid var(--ink);border-radius:50%;padding:0 3px}
  .front-author{
    position:absolute;top:523px;left:0;width:377px;text-align:center;
    font-family:"Montserrat",sans-serif;font-weight:700;font-size:16px;letter-spacing:.62em;color:var(--ink);
  }
</style>
</head>
<body>
<svg width="0" height="0" style="position:absolute">
  <defs>
    <linearGradient id="gold" x1="0" y1="0" x2="0" y2="1">
      <stop offset="0" stop-color="#f1d36a"/>
      <stop offset=".45" stop-color="#d9a92a"/>
      <stop offset="1" stop-color="#8a6a12"/>
    </linearGradient>
  </defs>
</svg>

<main class="wrap">
  <section class="panel back-cover">
    <p class="kicker top">Finding the</p>
    <svg class="title-word" width="215" height="84" viewBox="0 0 215 84"><text x="0" y="82" font-size="100" textLength="215" lengthAdjust="spacingAndGlyphs">STEADFAST</text></svg>
    <p class="kicker sub">Female Athlete</p>

    <div class="blurb">
      <p><strong>Finding the Steadfast Female Athlete</strong> is more than a book about training; it’s a call to action for parents, coaches, and anyone who wants to see girls rise strong in sport and in life.</p>
      <p>Grounded in years of coaching experience and real conversations with athletes and parents, this book delivers practical, no-fluff guidance on what young female athletes truly need: smart nutrition, intentional recovery, habits of success, and a mindset that holds strong under pressure.</p>
      <p>Whether she’s stepping onto the field for the first time or chasing down scholarships, this book equips you to lead her well at home, in the stands, and through every stage of her journey. Because being STEADFAST isn’t just how she plays, it’s about who she becomes.</p>
      <h2 class="about-heading">About the author</h2>
      <div class="author-photo" role="img" aria-label="Portrait photo of the author"></div>
      <p>Jordan Hale, CSCS, is the owner of Forward Motion Fitness in Maple Falls, Ohio, where he’s spent the last decade helping over 1,000 female athletes maximize performance, minimize injury risk, and build steadfast confidence.</p>
      <p>A former collegiate athlete turned performance coach, Jordan’s passion for training female athletes began after working with a young soccer player recovering from ACL surgery a moment that transformed his career and ignited a mission to change the way girls are trained and developed.</p>
      <p>Jordan believes every girl deserves the confidence to know she’s capable, strong, and created with purpose. He is also an author and speaker, presenting to schools and companies, as well as at the Peak Strength Coaching Summit, where he shares his expertise in developing strong, resilient female</p>
    </div>

    <div class="imprint"><span class="dot"></span><span>STEADFAST FEMALE ATHLETE</span></div>
  </section>

  <section class="panel spine">
    <p class="spine-title">FINDING THE <span class="gold">STEADFAST</span> FEMALE ATHLETE</p>
    <span class="spine-mark"></span>
    <p class="spine-author">JORDAN HALE</p>
  </section>

  <section class="panel front-cover">
    <div class="cover-photo" role="img" aria-label="Photo of a female athlete seen from behind, braided ponytail, tank top, dark moody lighting"></div>
    <p class="kicker top">Finding the</p>
    <svg class="title-word" width="315" height="128" viewBox="0 0 315 128"><text x="0" y="126" font-size="150" textLength="315" lengthAdjust="spacingAndGlyphs">STEADFAST</text></svg>
    <p class="kicker sub">Female Athlete</p>
    <p class="tagline">The <span class="ring">Athlete’s</span> playbook to<br>train strong, compete hard,<br>and build confidence in sports<br>and life</p>
    <p class="front-author">JORDAN HALE</p>
  </section>
</main>
</body>
</html>
```